LumaMove In-home Personal Training

I would like to have some eye-catching business card design. Opened to any ideas.

The business idea: mobile fitness - train clients at their places

Target Market(s)

General population, 20-60 years old

Industry/Entity Type

Fitness

Contact Information for Business Card

The information to include:
Name: Marta
Call or text: 306-555-0187
Website: LumaMove.ca
Please use the attached logo

Requirements
Should not have
• No orange or purple colours please

```html
<!DOCTYPE html>
<html lang="en">
<head>
<meta charset="utf-8">
<title>LumaMove Business Card</title>
<link href="https://fonts.googleapis.com/css2?family=Work+Sans:wght@300;400;500&display=swap" rel="stylesheet">
<style>
  :root {
    --backdrop: #2a2a2b;
    --card-dark: #48484a;
    --card-light: #ffffff;
    --ink: #3a3a3c;
    --ink-soft: #555557;
    --white: #ffffff;
  }
  * { margin: 0; padding: 0; box-sizing: border-box; }
  html, body {
    width: 1200px; height: 900px; overflow: hidden;
    background: var(--backdrop);
    font-family: "Work Sans", Arial, sans-serif;
  }
  .canvas {
    position: relative; width: 1200px; height: 900px;
    display: flex; flex-direction: column; align-items: center;
    justify-content: center; gap: 40px;
  }
  .card {
    position: relative; width: 700px; height: 400px;
    border-radius: 22px; overflow: hidden;
    box-shadow: 0 14px 30px rgba(0,0,0,0.45);
  }
  .card-front {
    background: var(--card-dark);
    display: flex; flex-direction: column; justify-content: center;
    padding-left: 150px;
  }
  .brand-name {
    color: var(--white); font-weight: 300;
    font-size: 92px; letter-spacing: 10px; line-height: 1;
  }
  .brand-tagline {
    color: var(--white); font-weight: 300;
    font-size: 15px; letter-spacing: 5.5px; margin-top: 14px;
    text-transform: uppercase;
  }
  .card-back { background: var(--card-light); }
  .side-band {
    position: absolute; left: 0; top: 0; bottom: 0; width: 120px;
    background: var(--card-dark);
    display: flex; align-items: center; justify-content: center;
  }
  .side-band-name {
    color: var(--white); font-weight: 300; font-size: 16px; letter-spacing: 1px;
  }
  .side-rule {
    position: absolute; top: 0; bottom: 0; left: 132px; width: 6px;
    background: var(--card-dark);
  }
  .person {
    position: absolute; left: 210px; top: 120px; color: var(--ink);
  }
  .person-name { font-size: 56px; font-weight: 400; letter-spacing: 4px; line-height: 1; }
  .person-role { font-size: 17px; font-weight: 500; margin-top: 2px; color: var(--ink-soft); }
  .contact {
    position: absolute; left: 196px; bottom: 42px; list-style: none; color: var(--ink);
  }
  .contact-item {
    display: flex; align-items: center; gap: 12px;
    font-size: 24px; letter-spacing: 2px; line-height: 34px;
  }
  .contact-icon { width: 22px; height: 22px; flex: none; }
</style>
</head>
<body>
<main class="canvas">
  <section class="card card-front">
    <div class="brand-name">LumaMove</div>
    <div class="brand-tagline">In-home personal training</div>
  </section>

  <section class="card card-back">
    <div class="side-band"><span class="side-band-name">LumaMove</span></div>
    <div class="side-rule"></div>
    <div class="person">
      <div class="person-name">Marta</div>
      <div class="person-role">Director</div>
    </div>
    <ul class="contact">
      <li class="contact-item">
        <svg class="contact-icon" viewBox="0 0 22 22" aria-hidden="true">
          <circle cx="11" cy="11" r="11" fill="#3a3a3c"/>
          <path d="M8 5.5c.6-.3 1.2 0 1.4.6l.7 2c.2.5 0 1-.4 1.3l-.8.5c.5 1.4 1.5 2.5 2.8 3.1l.6-.7c.4-.4.9-.5 1.4-.3l1.9.9c.5.3.7.9.4 1.4l-.5.9c-.4.7-1.2 1-2 .8-3.3-.9-5.8-3.6-6.5-7-.2-.8.2-1.6.9-2z" fill="#ffffff"/>
        </svg>
        <span>306-555-0187</span>
      </li>
      <li class="contact-item">
        <svg class="contact-icon" viewBox="0 0 22 22" aria-hidden="true">
          <circle cx="11" cy="11" r="11" fill="#3a3a3c"/>
          <rect x="5.5" y="7" width="11" height="8" rx="1" fill="none" stroke="#ffffff" stroke-width="1.4"/>
          <path d="M5.8 7.4 11 11.5l5.2-4.1" fill="none" stroke="#ffffff" stroke-width="1.4"/>
        </svg>
        <span>LumaMove.ca</span>
      </li>
    </ul>
  </section>
</main>
</body>
</html>
```